Marcus Tellow album cover "Borrowed Lanterns, Quiet Harbors"

3000x3000 album cover using attached image and provided text needed for cover of upcoming album for Seattle musician. Only front cover needed at this time.

Font styles to use
Serif
Sans Serif

Colors

Designer to choose colors to be used in the design.

```html
<!DOCTYPE html>
<html lang="en">
<head>
<meta charset="utf-8">
<title>Marcus Tellow – Borrowed Lanterns, Quiet Harbors</title>
<link rel="stylesheet" href="https://fonts.googleapis.com/css2?family=Tinos:wght@400&display=swap">
<style>
  :root {
    --sky-deep: #2a3557;
    --sky-violet: #5a5a8c;
    --haze: #8c8fb4;
    --lawn-dark: #1f4a2a;
    --lawn-bright: #4f9a3c;
    --lawn-glow: #7fcf63;
    --white: #ffffff;
    --rainbow: linear-gradient(90deg, #e0465a 0%, #e88a3c 18%, #d8c84a 34%, #6fcf7a 50%, #4fb6d8 66%, #7a7ad8 82%, #c464c8 100%);
  }
  html, body {
    margin: 0;
    padding: 0;
    width: 1200px;
    height: 1200px;
    overflow: hidden;
    background: #111;
  }
  .cover {
    position: relative;
    width: 1200px;
    height: 1200px;
    overflow: hidden;
    font-family: "Tinos", "Times New Roman", serif;
  }
  .cover-photo {
    position: absolute;
    inset: 0;
    background:
      radial-gradient(ellipse 38% 22% at 48% 52%, rgba(215, 210, 235, 0.75), rgba(215, 210, 235, 0) 70%),
      radial-gradient(ellipse 45% 35% at 85% 25%, rgba(120, 190, 140, 0.45), rgba(120, 190, 140, 0) 70%),
      radial-gradient(ellipse 60% 30% at 30% 90%, rgba(127, 207, 99, 0.55), rgba(127, 207, 99, 0) 70%),
      linear-gradient(180deg, var(--sky-deep) 0%, var(--sky-violet) 30%, var(--haze) 45%, var(--lawn-bright) 70%, var(--lawn-dark) 100%);
  }
  .artist-name {
    position: absolute;
    left: 52px;
    top: 40px;
    margin: 0;
    font-size: 142px;
    font-weight: 400;
    line-height: 1;
    color: var(--white);
    letter-spacing: -1px;
  }
  .album-title {
    position: absolute;
    left: 56px;
    top: 292px;
    margin: 0;
    font-size: 48px;
    font-weight: 400;
    line-height: 1;
    color: var(--white);
  }
  .title-stack span {
    position: absolute;
    line-height: 1;
    white-space: nowrap;
    background: var(--rainbow);
    -webkit-background-clip: text;
    background-clip: text;
    color: transparent;
  }
  .title-word-1 { left: 343px; top: 884px; font-size: 54px; }
  .title-word-2 { left: 708px; top: 950px; font-size: 60px; }
  .title-word-3 { left: 456px; top: 1036px; font-size: 92px; }
  .title-word-4 { left: 770px; top: 1078px; font-size: 110px; }
  .edge-title {
    position: absolute;
    right: 4px;
    top: 740px;
    font-size: 50px;
    line-height: 1;
    writing-mode: vertical-rl;
    opacity: 0.35;
    background: var(--rainbow);
    -webkit-background-clip: text;
    background-clip: text;
    color: transparent;
  }
</style>
</head>
<body>
  <main class="cover">
    <div class="cover-photo" role="img" aria-label="Dreamy, glitch-layered photograph of a small vintage camper trailer in a lush green garden at dusk, with trees and a fence behind"></div>
    <h1 class="artist-name">Marcus Tellow</h1>
    <h2 class="album-title">Borrowed Lanterns, Quiet Harbors</h2>
    <div class="title-stack" aria-hidden="true">
      <span class="title-word-1">Borrowed</span>
      <span class="title-word-2">Lanterns,</span>
      <span class="title-word-3">Quiet</span>
      <span class="title-word-4">Harbors</span>
    </div>
    <div class="edge-title" aria-hidden="true">Quiet Harbors</div>
  </main>
</body>
</html>
```